Financial Planning Firm looking for stationary design using new logo

Need stationary design using our new logo. We are a financial planning firm focused on the planning needs of retirees. Design should incorporate our new logo and its colors. The design should communicate a feeling of stability and security.
Have attached our new logo, as well as our old stationary for reference, letterhead, envelope and business card (but don't rely on for your design). Although the following disclosure must be present on all items "Securities and advisory services offered through Brindle Capital Alliance LLC, member DOVEX/TALQ. Brindle is under seperate ownership from any other named entity." in minimum 8 size font. you can see our old stationary for idea of disclosure placement. The business card (front and back) is in the middle of our letterhead sample if it is hard to tell.

```html
<!DOCTYPE html>
<html lang="en">
<head>
<meta charset="utf-8">
<title>Harlan T. Voss Financial Group LLC — Envelope</title>
<link rel="stylesheet" href="https://fonts.googleapis.com/css2?family=Open+Sans:wght@400&display=swap">
<style>
  :root {
    --backdrop: #e9e9ea;
    --paper: #f7f7f7;
    --paper-edge: #dcdcdc;
    --flap: #f1f1f1;
    --navy: #184c6e;
    --charcoal: #3a3838;
    --text-grey: #555;
  }
  * { box-sizing: border-box; margin: 0; padding: 0; }
  html, body { width: 1200px; height: 909px; overflow: hidden; }
  body {
    background: var(--backdrop);
    font-family: "Open Sans", Arial, sans-serif;
    display: flex; flex-direction: column; align-items: center;
    justify-content: center; gap: 44px;
  }
  .envelope {
    position: relative;
    width: 900px; height: 390px;
    background: var(--paper);
    border: 1px solid var(--paper-edge);
    box-shadow: 0 6px 18px rgba(0,0,0,.08);
    overflow: hidden;
  }
  .mark-circle {
    display: block; border-radius: 50%;
    background: var(--navy); flex: none;
  }

  /* Back */
  .flap {
    position: absolute; left: 0; top: 0; width: 100%; height: 175px;
    background: var(--flap);
    border-bottom: 1px solid var(--paper-edge);
    border-radius: 0 0 22px 22px;
    box-shadow: 0 2px 4px rgba(0,0,0,.06);
  }
  .flap .mark-circle {
    position: absolute; left: 50%; top: 88px;
    width: 34px; height: 34px; transform: translate(-50%, -50%);
  }
  .disclosure {
    position: absolute; left: 0; right: 0; top: 205px;
    text-align: center; font-size: 11px; line-height: 1.45; color: var(--text-grey);
  }

  /* Front */
  .sender {
    position: absolute; left: 34px; top: 36px;
    display: flex; align-items: flex-start; gap: 14px;
  }
  .sender .mark-circle { width: 46px; height: 46px; }
  .firm-name {
    font-size: 17px; font-weight: 400; line-height: 1.2; color: var(--navy);
  }
  .tagline {
    margin-top: 3px; font-size: 9px; line-height: 1.3; color: var(--text-grey);
  }
  .address {
    margin-top: 10px; font-size: 11px; line-height: 1.5; color: var(--text-grey);
  }
  .edge-band {
    position: absolute; left: 0; bottom: 0; width: 100%; height: 16px;
    display: flex; gap: 5px;
  }
  .band-navy { flex: 0 0 76%; background: var(--navy); }
  .band-charcoal { flex: 1; background: var(--charcoal); }
</style>
</head>
<body>
  <section class="envelope envelope-back" aria-label="Envelope back">
    <div class="flap">
      <span class="mark-circle"></span>
    </div>
    <p class="disclosure">
      Securities and advisory services offered through Brindle Capital Alliance LLC, member DOVEX/TALQ.<br>
      Brindle is under separate ownership from any other named entity.
    </p>
  </section>

  <section class="envelope envelope-front" aria-label="Envelope front">
    <div class="sender">
      <span class="mark-circle"></span>
      <div class="sender-text">
        <h1 class="firm-name">Harlan T. Voss<br>Financial Group LLC</h1>
        <p class="tagline">Security for your future</p>
        <p class="address">4420 Harbor Lane, Suite 310<br>Ashford, WA 98017</p>
      </div>
    </div>
    <div class="edge-band">
      <span class="band-navy"></span>
      <span class="band-charcoal"></span>
    </div>
  </section>
</body>
</html>
```